Brightpath Desk letterhead and envelope

Design a formal (8.5x11) letterhead and envelope for sales outreach and legal matters. Using design input from https://www.brightpathdesk.com/ and the attached documents.

Industry/Entity Type

Software Service

Requirements
Must have
• These 4 hex colors are our official colors:
• #355c98 [blue]
• #1eb1a2 [teal]
• #fdba12 [gold]
• #f1653b [orange]
• So no other colors besides these should be used.

```html
<!DOCTYPE html>
<html lang="en">
<head>
<meta charset="utf-8">
<title>Brightpath Desk Letterhead</title>
<link href="https://fonts.googleapis.com/css2?family=Lato:wght@300;400;700&family=Arimo&family=Yellowtail&display=swap" rel="stylesheet">
<style>
  :root{
    --blue:#355c98;
    --teal:#1eb1a2;
    --ink:#4a4a4a;
    --ink-dark:#222;
    --paper:#ffffff;
  }
  *{margin:0;padding:0;box-sizing:border-box;}
  html,body{width:996px;height:1200px;overflow:hidden;background:var(--paper);}
  .letterhead{position:relative;width:996px;height:1200px;background:var(--paper);font-family:'Lato',sans-serif;color:var(--ink);}
  .brand{position:absolute;left:81px;top:40px;display:flex;align-items:center;gap:16px;}
  .brand-dot{width:56px;height:56px;border-radius:50%;background:var(--blue);}
  .brand-name{font-family:'Lato',sans-serif;font-weight:300;font-size:48px;color:var(--blue);letter-spacing:0.5px;}
  .contact{position:absolute;left:734px;top:24px;padding-left:14px;border-left:1px solid #bfc6d2;font-family:'Arimo',sans-serif;font-size:14.5px;color:var(--ink-dark);list-style:none;}
  .contact li{display:flex;align-items:center;gap:6px;height:24.5px;}
  .contact svg{width:15px;height:15px;flex:none;}
  .salutation{position:absolute;left:83px;top:266px;font-weight:700;font-size:18px;color:var(--blue);}
  .body{position:absolute;left:83px;top:313px;width:828px;font-size:18.3px;line-height:27px;}
  .body p{margin-bottom:21px;}
  .body span{display:block;text-align:justify;text-align-last:justify;}
  .body span:last-child{text-align-last:left;}
  .closing{position:absolute;left:83px;top:797px;font-size:20px;color:var(--ink-dark);}
  .signature{position:absolute;left:81px;top:832px;font-family:'Yellowtail',cursive;font-size:38px;color:var(--blue);}
  .address{position:absolute;left:83px;top:1142px;display:flex;align-items:center;gap:5px;font-family:'Arimo',sans-serif;font-size:14.5px;color:var(--ink-dark);}
  .address svg{width:14px;height:14px;}
  .footer-band{position:absolute;left:0;bottom:0;width:996px;height:22px;}
</style>
</head>
<body>
<main class="letterhead">
  <header>
    <div class="brand">
      <span class="brand-dot"></span>
      <span class="brand-name">Brightpath Desk</span>
    </div>
    <ul class="contact">
      <li><svg viewBox="0 0 16 16"><circle cx="8" cy="8" r="7" fill="none" stroke="var(--blue)" stroke-width="1.3"/><rect x="5.5" y="4" width="5" height="8" rx="1" fill="none" stroke="var(--blue)" stroke-width="1.2"/></svg>(555) 214-0396</li>
      <li><svg viewBox="0 0 16 16"><circle cx="8" cy="8" r="7" fill="none" stroke="var(--blue)" stroke-width="1.3"/><path d="M5 4.5l1.6-.3 1 2-1 .8a5 5 0 0 0 2.4 2.4l.8-1 2 1-.3 1.6c-3.5.3-6.8-3-6.5-6.5z" fill="var(--blue)"/></svg>(555) 860-4172(Main)</li>
      <li><svg viewBox="0 0 16 16"><circle cx="8" cy="8" r="7" fill="none" stroke="var(--blue)" stroke-width="1.3"/><rect x="4.2" y="5.5" width="7.6" height="5.2" fill="none" stroke="var(--blue)" stroke-width="1.2"/><path d="M4.2 5.5L8 8.4l3.8-2.9" fill="none" stroke="var(--blue)" stroke-width="1.2"/></svg>jsmith@brightpathdesk.com</li>
      <li><svg viewBox="0 0 16 16"><g fill="none" stroke="var(--blue)" stroke-width="1.2"><circle cx="8" cy="8" r="7"/><ellipse cx="8" cy="8" rx="3" ry="7"/><path d="M1 8h14M2.5 4.5h11M2.5 11.5h11"/></g></svg>www.brightpathdesk.com</li>
    </ul>
  </header>

  <p class="salutation">Dear Mr. Lorem,</p>

  <section class="body">
    <p><span>Lorem ipsum dolor sit amet, consectetuer adipiscing elit, sed diam nonummy nibh euismod tinci-</span><span>dunt ut laoreet dolore magna aliquam erat volutpat. Ut wisi enim ad minim veniam, quis nostrud</span><span>exerci tation ullamcorper suscipit lobortis nisl ut aliquip ex ea commodo consequat. Duis autem vel</span><span>eum iriure dolor in hendiusto odio dignissim qui blandit praesent luptatum zzril delenit augue duis</span><span>dolore te feugait nulla facilisi.</span></p>
    <p><span>Lorem ipsum dolor sit amet, consectetuer adipiscing elit, sed diam nonummy nibh euismod tinci-</span><span>dunt ut laoreet dolore magna aliquam erat volutpat. Ut wisi enim ad minim veniam, quis nostrud</span><span>exerci tation ullamcorper suscipit lobortis nisl ut aliquip ex ea commodo consequat. Duis autem vel</span><span>eum iriure dolor in hendiusto odio dignissim qui blandit praesent luptatum zzril delenit augue duis</span><span>dolore te feugait nulla facilisi.</span></p>
    <p><span>Lorem ipsum dolor sit amet, consectetuer adipiscing elit, sed diam nonummy nibh euismod tinci-</span><span>dunt ut laoreet dolore magna aliquam erat volutpat. Ut wisi enim ad minim veniam, quis nostrud</span><span>exerci tation ullamcorper suscipit lobortis nisl ut aliquip ex ea commodo consequat. Duis autem vel</span><span>eum iriure dolor in hendiusto odio dignissim qui blandit praesent luptatum zzril delenit augue duis</span><span>dolore te feugait nulla facilisi.</span></p>
  </section>

  <p class="closing">Sincerely Your,</p>
  <p class="signature">Your Name</p>

  <footer>
    <p class="address"><svg viewBox="0 0 16 16"><circle cx="8" cy="8" r="7" fill="none" stroke="var(--blue)" stroke-width="1.3"/><path d="M8 12.5S5 9.2 5 7a3 3 0 0 1 6 0c0 2.2-3 5.5-3 5.5z" fill="var(--blue)"/><circle cx="8" cy="7" r="1" fill="var(--paper)"/></svg>42 Lantern Row, Fairhaven, OH 45102</p>
    <svg class="footer-band" viewBox="0 0 996 22" preserveAspectRatio="none">
      <polygon points="0,4 498,4 482,22 0,22" fill="var(--blue)"/>
      <polygon points="508,0 996,0 996,22 490,22" fill="var(--teal)"/>
    </svg>
  </footer>
</main>
</body>
</html>
```